Tech Startup Needs Business Card Design

I am looking for an eye catching business card design for our new company, Torn Kite. We are a place for business owners and contractors to share their experiences with their customers and check their current customers. Our website, www.torn-kite.co, may be able to offer some guidance as to the design.

Industry/Entity Type

Business

Contact Information for Business Card

Owen Barthwick
888-417-3083
Owen@torn-kite.co
www.torn-kite.co

```html
<!DOCTYPE html>
<html lang="en">
<head>
<meta charset="utf-8">
<title>Torn Kite — Business Card</title>
<link rel="stylesheet" href="https://fonts.googleapis.com/css2?family=Comfortaa:wght@700&display=swap">
<style>
  :root {
    --backdrop: #3c3e3d;
    --card-white: #ffffff;
    --card-frost: #c9cccb;
    --brand-red: #d7141c;
    --brand-green: #148a3a;
    --ink: #111111;
    --on-red: #ffffff;
  }
  html, body {
    margin: 0;
    width: 1200px;
    height: 800px;
    overflow: hidden;
    background: var(--backdrop);
    font-family: "Comfortaa", "Varela Round", sans-serif;
  }
  .business-card {
    position: absolute;
    left: 180px;
    top: 160px;
    width: 840px;
    height: 480px;
    border-radius: 14px;
    overflow: hidden;
    background: linear-gradient(90deg, var(--card-white) 0%, var(--card-white) 62%, #eef0ef 72%, var(--card-frost) 100%);
    box-shadow: 0 20px 40px rgba(0,0,0,0.35);
  }
  .brand {
    position: absolute;
    left: 56px;
    top: 52px;
    display: flex;
    align-items: center;
    gap: 14px;
  }
  .brand-dot {
    width: 30px;
    height: 30px;
    border-radius: 50%;
    background: var(--brand-red);
  }
  .brand-name {
    font-size: 46px;
    font-weight: 700;
    color: var(--ink);
    letter-spacing: -0.5px;
    line-height: 1;
  }
  .decor-disc {
    position: absolute;
    left: 520px;
    top: 110px;
    width: 300px;
    height: 300px;
    border-radius: 50%;
    background: var(--brand-red);
  }
  .person-name {
    position: absolute;
    left: 60px;
    top: 176px;
    width: 410px;
    margin: 0;
    text-align: right;
    font-size: 38px;
    font-weight: 700;
    color: var(--brand-green);
  }
  .contact-band {
    position: absolute;
    left: 0;
    top: 240px;
    width: 480px;
    height: 116px;
    background: var(--brand-red);
    border-radius: 0 34px 34px 0;
    list-style: none;
    margin: 0;
    padding: 16px 26px 0 0;
    box-sizing: border-box;
  }
  .contact-line {
    display: flex;
    justify-content: flex-end;
    align-items: center;
    gap: 14px;
    height: 42px;
    color: var(--on-red);
    font-size: 23px;
    font-weight: 700;
  }
  .contact-icon {
    width: 30px;
    height: 30px;
    flex: none;
  }
</style>
</head>
<body>
  <article class="business-card">
    <div class="decor-disc" aria-hidden="true"></div>

    <header class="brand">
      <span class="brand-dot" aria-hidden="true"></span>
      <span class="brand-name">Torn Kite</span>
    </header>

    <h1 class="person-name">Owen Barthwick</h1>

    <ul class="contact-band">
      <li class="contact-line">
        <span>888-417-3083</span>
        <svg class="contact-icon" viewBox="0 0 30 30" aria-label="phone">
          <circle cx="15" cy="15" r="13" fill="none" stroke="#fff" stroke-width="2"/>
          <path d="M11 8.5c-.8 0-2 1.2-1.8 2.6.5 3.8 4.9 8.4 8.8 9.2 1.3.3 2.7-.9 2.7-1.7l-.1-1-2.6-1.2-1.3 1.3c-1.8-.7-3.3-2.3-4-4l1.3-1.3L12.9 8.7z" fill="#fff"/>
        </svg>
      </li>
      <li class="contact-line">
        <span>Owen@torn-kite.co</span>
        <svg class="contact-icon" viewBox="0 0 30 30" aria-label="email">
          <circle cx="15" cy="15" r="13" fill="none" stroke="#fff" stroke-width="2"/>
          <rect x="8.5" y="10" width="13" height="10" rx="1" fill="#fff"/>
          <path d="M8.5 10.5 15 15.5l6.5-5" fill="none" stroke="#d7141c" stroke-width="1.5"/>
        </svg>
      </li>
    </ul>
  </article>
</body>
</html>
```